Veterinarian specialized in Equine (horse) sports medicine needs logo and stationary design!

New veterinary clinic only focused on horses needs logo and stationary designs. The clinic works with sport horses including jumping horses, dressage horses and polo horses (all disciplines you can find online. No racing horses). Name of clinic is StrideCare and is based in Mexico City where there is a large and elite clientele of sports horses. My main focus is orthopedics and rehabilitation.
I think logo should include horse(s), especially if they are performing a sport (like jumping, etc).

Target Market(s)

Elite horse-owners of sport horses.

Industry/Entity Type

Horseback Riding

Requirements
Must have
• Great Logo! I like bold and bright colors (no pastels), but with a professional tone.

```html
<!DOCTYPE html>
<html lang="en">
<head>
<meta charset="utf-8">
<title>StrideCare Stationery</title>
<link href="https://fonts.googleapis.com/css2?family=Open+Sans:wght@400;600;700&display=swap" rel="stylesheet">
<style>
  :root{
    --brand-blue:#1266b8;
    --brand-red:#d8262e;
    --paper:#ffffff;
    --backdrop:#e4e8f1;
    --ink:#2b2b2b;
    --muted:#6b7a90;
  }
  *{box-sizing:border-box;margin:0;padding:0}
  html,body{width:1200px;height:800px;overflow:hidden}
  body{background:var(--backdrop);font-family:"Open Sans",Arial,sans-serif;color:var(--ink);position:relative}
  .sheet{position:absolute;background:var(--paper)}
  .sheet--blue{background:var(--brand-blue)}

  /* brand lockup */
  .brand{display:flex;flex-direction:column;align-items:flex-start}
  .brand__row{display:flex;align-items:center;gap:3px}
  .brand__square{background:var(--brand-blue);display:block}
  .brand__name{font-weight:700;color:var(--brand-blue);line-height:1}
  .brand__sub{color:var(--brand-blue);letter-spacing:.18em;text-transform:uppercase;line-height:1.2}
  .brand--light .brand__name,.brand--light .brand__sub{color:#fff}
  .brand--light .brand__square{background:#fff}
  .brand--center{align-items:center}

  .services{color:var(--brand-blue);text-transform:uppercase;letter-spacing:.06em;white-space:nowrap}
  .services .dot{color:var(--brand-red);margin:0 2px}
  .services--light{color:#fff}

  /* letterhead */
  .letterhead{width:250px;height:340px}
  .letterhead .brand{position:absolute;left:26px;top:20px}
  .letterhead .brand__square{width:18px;height:18px}
  .letterhead .brand__name{font-size:7px}
  .letterhead .brand__sub{font-size:2.6px}
  .contact{position:absolute;right:28px;top:20px;font-size:3px;line-height:1.45;color:var(--ink)}
  .letter{position:absolute;left:26px;top:86px;width:200px;font-size:3.6px;line-height:1.42}
  .letter p{margin-bottom:4.5px}
  .signature{width:48px;height:9px;background:linear-gradient(90deg,#3a3a3a22,#3a3a3a55,#3a3a3a22);border-radius:4px;margin:2px 0 1px}
  .letterhead .services{position:absolute;left:0;right:0;bottom:8px;text-align:center;font-size:3px}
  .letterhead__rule{position:absolute;left:0;right:0;bottom:0;height:3px;display:flex}
  .letterhead__rule span:first-child{flex:1;background:var(--brand-blue)}
  .letterhead__rule span:last-child{width:48px;background:var(--brand-red)}

  /* envelopes */
  .envelope{width:260px;height:126px}
  .envelope .brand{position:absolute;left:12px;top:12px}
  .envelope .brand__square{width:18px;height:18px}
  .envelope .brand__name{font-size:6.5px}
  .envelope .brand__sub{font-size:2.4px}
  .envelope .services{position:absolute;left:0;right:0;bottom:6px;text-align:center;font-size:3px}
  .envelope__flap{position:absolute;left:0;top:0}
  .envelope__flap-mark{position:absolute;left:122px;top:26px;width:16px;height:16px;background:#1b6fc2}

  /* cards */
  .card{width:107px;height:58px}
  .card--front{display:flex;flex-direction:column;align-items:center;justify-content:center}
  .card--front .brand__square{width:10px;height:10px}
  .card--front .brand__name{font-size:7px}
  .card--front .brand__sub{font-size:2.4px}
  .card--front .services{position:absolute;bottom:7px;font-size:2.3px}
  .card--back .brand{position:absolute;left:14px;top:18px}
  .card--back .brand__square{width:13px;height:13px}
  .card--back .brand__name{font-size:4.6px}
  .card--back .brand__sub{font-size:1.8px}
  .card__divider{position:absolute;left:61px;top:18px;width:.6px;height:22px;background:var(--brand-blue)}
  .card__details{position:absolute;left:64px;top:18px;font-size:2.6px;line-height:1.4;color:var(--ink)}
  .card__person{font-weight:700;color:var(--brand-blue);font-size:3.4px;text-transform:uppercase}

  /* folder */
  .folder{width:297px;height:360px}
  .folder .brand{position:absolute;left:0;right:0;top:138px}
  .folder .brand__square{width:62px;height:62px;margin-bottom:4px}
  .folder .brand__name{font-size:12px}
  .folder .brand__sub{font-size:4px;margin-top:2px}
  .folder .services{position:absolute;left:0;right:0;bottom:26px;text-align:center;font-size:5.6px}
  .folder__web{position:absolute;left:0;right:0;bottom:13px;text-align:center;font-size:5.6px;color:#fff}

  /* square brochure */
  .brochure{width:146px;height:142px}
  .brochure .brand{position:absolute;left:0;right:0;top:40px}
  .brochure .brand__square{width:50px;height:50px;margin-bottom:4px}
  .brochure .brand__name{font-size:9px}
  .brochure .brand__sub{font-size:3px;margin-top:2px}
  .brochure .services{position:absolute;left:0;right:0;bottom:8px;text-align:center;font-size:3.2px}

  /* compliments slip */
  .compliments{width:247px;height:112px}
  .compliments .brand{position:absolute;left:16px;top:14px}
  .compliments .brand__square{width:30px;height:30px;margin-bottom:3px}
  .compliments .brand__name{font-size:6px}
  .compliments .brand__sub{font-size:2.3px}
  .compliments__title{position:absolute;right:16px;bottom:18px;font-size:10px;font-weight:700;color:var(--brand-blue)}
</style>
</head>
<body>

<!-- letterhead, upper left -->
<section class="sheet letterhead" style="left:154px;top:26px">
  <div class="brand">
    <span class="brand__square"></span>
    <div class="brand__name" style="margin-top:3px">StrideCare</div>
    <div class="brand__sub">Veterinary Clinic</div>
  </div>
  <address class="contact" style="font-style:normal">
    Calle Prado 118, Lomas<br>Ciudad de México 11000<br>t: +52 55 0000 1234<br>e: hola@stridecare-vet.mx<br>w: www.stridecare-vet.mx
  </address>
  <article class="letter">
    <p>November 1, 2015<br>Mr. Lucas Ortega<br>1234 Avenida Reforma<br>Ciudad de México 11000</p>
    <p>Dear Mr. Ortega,<br>Thank you for choosing our clinic for your horse's care. This letter confirms the plan we discussed during the first visit and the next steps.</p>
    <p>Our team will begin with a full gait assessment, followed by imaging of the left foreleg. Results will guide a tailored rehabilitation program, with weekly check-ins and clear goals for return to training.</p>
    <p>Please contact us with any questions about scheduling, fees or aftercare. We are happy to coordinate with your trainer and farrier.</p>
    <p>We look forward to seeing your horse back in the arena soon.</p>
    <p>Sincerely,</p>
    <div class="signature" role="img" aria-label="Handwritten signature"></div>
    <div>President</div>
  </article>
  <div class="services">Surgery <span class="dot">•</span> First Aid <span class="dot">•</span> Orthipedic <span class="dot">•</span> Rehabilitation</div>
  <div class="letterhead__rule"><span></span><span></span></div>
</section>

<!-- envelope front -->
<section class="sheet envelope" style="left:458px;top:83px">
  <div class="brand">
    <span class="brand__square"></span>
    <div class="brand__name" style="margin-top:3px">StrideCare</div>
    <div class="brand__sub">Veterinary Clinic</div>
  </div>
  <div class="services">Surgery <span class="dot">•</span> First Aid <span class="dot">•</span> Orthipedic <span class="dot">•</span> Rehabilitation</div>
</section>

<!-- envelope back -->
<section class="sheet envelope" style="left:733px;top:82px">
  <svg class="envelope__flap" width="260" height="36" viewBox="0 0 260 36">
    <polygon points="0,0 260,0 244,36 16,36" fill="var(--brand-blue)"/>
  </svg>
  <span class="envelope__flap-mark"></span>
</section>

<!-- letterhead, centre -->
<section class="sheet letterhead" style="left:464px;top:262px">
  <div class="brand">
    <span class="brand__square"></span>
    <div class="brand__name" style="margin-top:3px">StrideCare</div>
    <div class="brand__sub">Veterinary Clinic</div>
  </div>
  <address class="contact" style="font-style:normal">
    Calle Prado 118, Lomas<br>Ciudad de México 11000<br>t: +52 55 0000 1234<br>e: hola@stridecare-vet.mx<br>w: www.stridecare-vet.mx
  </address>
  <article class="letter">
    <p>November 1, 2015<br>Mr. Lucas Ortega<br>1234 Avenida Reforma<br>Ciudad de México 11000</p>
    <p>Dear Mr. Ortega,<br>Thank you for choosing our clinic for your horse's care. This letter confirms the plan we discussed during the first visit and the next steps.</p>
    <p>Our team will begin with a full gait assessment, followed by imaging of the left foreleg. Results will guide a tailored rehabilitation program, with weekly check-ins and clear goals for return to training.</p>
    <p>Please contact us with any questions about scheduling, fees or aftercare. We are happy to coordinate with your trainer and farrier.</p>
    <p>We look forward to seeing your horse back in the arena soon.</p>
    <p>Sincerely,</p>
    <div class="signature" role="img" aria-label="Handwritten signature"></div>
    <div>President</div>
  </article>
  <div class="services">Surgery <span class="dot">•</span> First Aid <span class="dot">•</span> Orthipedic <span class="dot">•</span> Rehabilitation</div>
  <div class="letterhead__rule"><span></span><span></span></div>
</section>

<!-- business card front -->
<section class="sheet sheet--blue card card--front" style="left:874px;top:280px">
  <div class="brand brand--light">
    <div class="brand__row">
      <span class="brand__square"></span>
      <span class="brand__name">StrideCare</span>
    </div>
  </div>
  <div class="services services--light">Surgery · First Aid · Orthipedic · Rehabilitation</div>
</section>

<!-- business card back -->
<section class="sheet card card--back" style="left:874px;top:374px">
  <div class="brand">
    <span class="brand__square"></span>
    <div class="brand__name" style="margin-top:2px">StrideCare</div>
    <div class="brand__sub">Veterinary Clinic</div>
  </div>
  <span class="card__divider"></span>
  <div class="card__details">
    <div class="card__person">Diego Márquez</div>
    <div>Senior Consultant</div>
    <div>m: +52 55 0000 5678</div>
    <div>t: +52 55 0000 1234</div>
    <div>hola@stridecare-vet.mx</div>
    <div>www.stridecare-vet.mx</div>
  </div>
</section>

<!-- presentation folder -->
<section class="sheet sheet--blue folder" style="left:110px;top:414px">
  <div class="brand brand--light brand--center">
    <span class="brand__square"></span>
    <div class="brand__name">StrideCare</div>
    <div class="brand__sub">Veterinary Clinic</div>
  </div>
  <div class="services services--light">Surgery <span class="dot">|</span> First Aid <span class="dot">|</span> Orthipedic <span class="dot">|</span> Rehabilitation</div>
  <div class="folder__web">www.stridecare-vet.mx</div>
</section>

<!-- compliments slip -->
<section class="sheet compliments" style="left:465px;top:646px">
  <div class="brand">
    <span class="brand__square"></span>
    <div class="brand__name">StrideCare</div>
    <div class="brand__sub">Veterinary Clinic</div>
  </div>
  <div class="compliments__title">With Compliments</div>
</section>

<!-- square brochure -->
<section class="sheet sheet--blue brochure" style="left:757px;top:521px">
  <div class="brand brand--light brand--center">
    <span class="brand__square"></span>
    <div class="brand__name">StrideCare</div>
    <div class="brand__sub">Veterinary Clinic</div>
  </div>
  <div class="services services--light">Surgery · First Aid · Orthipedic · Rehabilitation</div>
</section>

</body>
</html>
```